Tallyleaf Web Design

Create Website Design for Tallyleaf. Tallyleaf is online application for collaboration team work system (task list management). More concept design for this project please find attach file ("tallyleaf website concept.pdf") . But my concept is just describe minimal features not bind design

For tallyleaf logo, i had already attach files. But i had not decided what color i chose, so it's okay if you suggest logo color for your suitable website design.
Updates

Dear All Designer,

I like brisk carousel (http://quorvanlabs.example/brisk-carousel/),
may be your concept design can adjust with this concept.
but don't worry about script for brisk carousel, my team will be handle
You just make website design to suitable with brisk carousel

but if you had own website design concept are welcome

thanks

Target Market(s)

Business Company

Industry/Entity Type

Management

```html
<!DOCTYPE html>
<html lang="en">
<head>
<meta charset="utf-8">
<title>Tallyleaf — Online Collaboration Team Work</title>
<link rel="stylesheet" href="https://fonts.googleapis.com/css2?family=Oswald:wght@400;500&family=PT+Sans:wght@400;700&family=Ubuntu:wght@500&display=swap">
<style>
  :root {
    --lime: #a3d022;
    --lime-button: #9ccb1f;
    --nav-text: #3b5a12;
    --logo-ink: #1f4a55;
    --footer-green: #6b9a2b;
    --button-green: #6a9a2a;
    --heading-grey: #4a4a4a;
    --body-grey: #555;
    --white: #ffffff;
  }
  * { box-sizing: border-box; margin: 0; padding: 0; }
  html, body { width: 1200px; height: 890px; overflow: hidden; }
  body { position: relative; font-family: "PT Sans", sans-serif; background: #fff; }

  .site-header { position: absolute; inset: 0 0 auto 0; height: 118px; display: flex; z-index: 2; }
  .brand-area { width: 515px; background: var(--white); position: relative; }
  .brand { position: absolute; left: 178px; top: 36px; display: flex; align-items: center; gap: 10px; }
  .brand-name { font-family: "Ubuntu", sans-serif; font-weight: 500; font-size: 52px; color: var(--logo-ink); letter-spacing: -0.5px; }
  .brand-dot { width: 30px; height: 30px; border-radius: 50%; background: var(--lime); }
  .main-nav { flex: 1; background: var(--lime); position: relative; }
  .main-nav a { position: absolute; top: 70px; font-family: "Oswald", sans-serif; font-size: 17px; color: var(--nav-text); text-decoration: none; text-transform: uppercase; letter-spacing: 0.2px; }

  .hero-backdrop { position: absolute; left: 0; top: 118px; width: 1200px; height: 683px;
    background: radial-gradient(ellipse at 25% 30%, #c9b7a2 0%, transparent 45%),
                radial-gradient(ellipse at 80% 60%, #d7c7b2 0%, transparent 50%),
                linear-gradient(160deg, #4b5a75 0%, #8c8fa0 40%, #b7a896 70%, #6e6a78 100%); }

  .carousel { position: absolute; left: 0; top: 0; width: 1200px; height: 480px; }
  .carousel-back { position: absolute; left: 177px; top: 165px; width: 505px; height: 264px; background: var(--white); border-radius: 3px; }
  .carousel-back::after { content: ""; position: absolute; inset: 8px 9px; background: linear-gradient(90deg, #d9a463, #f0d6b1 20%, #f0d6b1 80%, #d9a463); }
  .carousel-frame { position: absolute; left: 205px; top: 149px; width: 450px; height: 295px; background: var(--white); border-radius: 3px; box-shadow: 0 2px 8px rgba(0,0,0,.35); }
  .slide-photo { position: absolute; left: 8px; top: 9px; width: 434px; height: 277px; background: linear-gradient(135deg, #8cc23a 0%, #d8e6a5 40%, #b7d46c 65%, #5d9a20 100%); }
  .play-button { position: absolute; left: 179px; top: 102px; }
  .carousel-dots { position: absolute; top: 470px; left: 398px; display: flex; gap: 8px; }
  .carousel-dots span { width: 9px; height: 9px; border-radius: 2px; background: var(--white); }
  .carousel-dots span.is-active { background: #444; }

  .hero-copy { position: absolute; left: 721px; top: 174px; width: 320px; color: var(--white); }
  .hero-copy h1 { font-family: "Oswald", sans-serif; font-weight: 400; font-size: 42px; line-height: 43px; text-transform: uppercase; }
  .hero-copy p { margin-top: 12px; font-size: 11.5px; line-height: 15px; width: 300px; }
  .pill-button { display: inline-block; margin-top: 18px; width: 130px; height: 39px; line-height: 39px; text-align: center; border-radius: 20px; background: var(--lime-button); color: #2f4a0c; font-size: 15px; text-decoration: none; }

  .feature { position: absolute; top: 516px; width: 270px; height: 252px; background: rgba(245,238,230,.72); border: 1px solid rgba(255,255,255,.6); }
  .feature-icon { position: absolute; left: 75px; top: 18px; width: 120px; height: 112px; border-radius: 6px; }
  .feature-divider { position: absolute; left: 0; right: 0; top: 149px; border-top: 1px solid rgba(255,255,255,.8); }
  .feature h2 { position: absolute; left: 22px; top: 162px; font-family: "Oswald", sans-serif; font-weight: 400; font-size: 18px; color: var(--heading-grey); }
  .feature p { position: absolute; left: 22px; top: 190px; width: 228px; font-size: 10px; line-height: 12.5px; color: var(--body-grey); text-align: justify; }
  .small-button { position: absolute; left: 22px; top: 220px; width: 70px; height: 20px; line-height: 20px; text-align: center; background: var(--button-green); border-top: 2px solid #8ec13b; color: var(--white); font-family: "Oswald", sans-serif; font-size: 11.5px; text-decoration: none; }

  .site-footer { position: absolute; left: 0; top: 801px; width: 1200px; height: 89px; background: var(--footer-green); }
  .footer-edge { position: absolute; left: 0; top: -4px; width: 1200px; height: 8px; background: radial-gradient(circle at 4px 4px, #fff 2.5px, transparent 3px) 0 0 / 8px 8px repeat-x; }
  .footer-links { position: absolute; left: 162px; top: 25px; font-size: 12px; color: var(--white); line-height: 16px; }
  .footer-links a { color: var(--white); text-decoration: none; }
  .footer-links .sep { margin: 0 4px; }
  .follow { position: absolute; left: 795px; top: 37px; display: flex; align-items: center; gap: 6px; }
  .follow-label { font-family: "Oswald", sans-serif; font-size: 16px; color: var(--white); margin-right: 6px; }
  .social-dot { width: 28px; height: 28px; border-radius: 50%; background: linear-gradient(#fff, #dcdcdc); box-shadow: 0 1px 2px rgba(0,0,0,.3); }
</style>
</head>
<body>
  <header class="site-header">
    <div class="brand-area">
      <div class="brand"><span class="brand-name">tallyleaf</span><span class="brand-dot"></span></div>
    </div>
    <nav class="main-nav">
      <a href="#" style="left:34px">Home</a>
      <a href="#" style="left:103px">Products</a>
      <a href="#" style="left:198px">Solutions</a>
      <a href="#" style="left:298px">Industries</a>
      <a href="#" style="left:400px">About Us</a>
      <a href="#" style="left:493px">Login</a>
    </nav>
  </header>

  <div class="hero-backdrop" role="img" aria-label="Blurred background photo of a team at work"></div>

  <section class="carousel">
    <div class="carousel-back"></div>
    <div class="carousel-frame">
      <div class="slide-photo" role="img" aria-label="Photo of a woman lying in the grass using a tablet"></div>
      <svg class="play-button" width="92" height="92" viewBox="0 0 92 92" aria-hidden="true">
        <circle cx="46" cy="46" r="45" fill="rgba(60,60,60,.6)" stroke="rgba(255,255,255,.35)" stroke-width="2"/>
        <path d="M35 26 L66 46 L35 66 Z" fill="#fff"/>
      </svg>
    </div>
    <div class="carousel-dots"><span></span><span class="is-active"></span><span></span><span></span></div>
  </section>

  <section class="hero-copy">
    <h1>Customize online<br>collaboration<br>team work</h1>
    <p>Lorem ipsum dolor sit amet, consectetuer adipiscing elit. Aenean commodo ligula eget dolor. Aenean massa. Cum sociis natoque penatibus et magnis dis parturient montes, nascetur ridiculus mus.</p>
    <a class="pill-button" href="#">View More...</a>
  </section>

  <article class="feature" style="left:162px">
    <div class="feature-icon" role="img" aria-label="Application folder icon" style="background:linear-gradient(#dbe6f0,#8faccc)"></div>
    <div class="feature-divider"></div>
    <h2>Customize Application</h2>
    <p>Lorem ipsum dolor sit amet, sectetuer adipiscing elit.Lorem ipsum dolor sit amet.</p>
    <a class="small-button" href="#">View More</a>
  </article>
  <article class="feature" style="left:457px">
    <div class="feature-icon" role="img" aria-label="Desktop computer icon" style="background:linear-gradient(135deg,#e6e6e6,#2f56d6 55%,#bfbfbf)"></div>
    <div class="feature-divider"></div>
    <h2>Synchronize All Device</h2>
    <p>Lorem ipsum dolor sit amet, sectetuer adipiscing elit.Lorem ipsum dolor sit amet.</p>
    <a class="small-button" href="#">View More</a>
  </article>
  <article class="feature" style="left:751px">
    <div class="feature-icon" role="img" aria-label="Clipboard report icon" style="background:linear-gradient(#c58a4a,#e9eef5 40%,#d93a3a)"></div>
    <div class="feature-divider"></div>
    <h2>Report</h2>
    <p>Lorem ipsum dolor sit amet, sectetuer adipiscing elit.Lorem ipsum dolor sit amet.</p>
    <a class="small-button" href="#">View More</a>
  </article>

  <footer class="site-footer">
    <div class="footer-edge"></div>
    <div class="footer-links">
      <a href="#">Home</a><span class="sep">|</span><a href="#">About Us</a><span class="sep">|</span><a href="#">Careers</a><span class="sep">|</span><a href="#">Terms &amp; Conditions</a><span class="sep">|</span><a href="#">Contact</a><br>
      Copyright © 2012. All Rights Reserved.
    </div>
    <div class="follow">
      <span class="follow-label">FOLLOW US ON</span>
      <span class="social-dot" aria-label="Feed"></span>
      <span class="social-dot" aria-label="Social network"></span>
      <span class="social-dot" aria-label="Social network"></span>
      <span class="social-dot" aria-label="Chat"></span>
    </div>
  </footer>
</body>
</html>
```